pelmora.com

Design proposals for a gold bank site and gold wallet main page. The site will let people (and companies) open accounts and purchase gold for deposit and later make payments with the gold they hold in the bank. The bank will be a e-money licensed venture located in Switzerland. The functionality of the "system" will be very simple and possibly only use icon symbols so it can be multilingual.

The mainstays of the site will be security and trust. Al digital gold is backed 100 % by visible gold in vault audited every day.

Target Market(s)

Asian and American gold buyers and people preferring gold to currency

Industry/Entity Type

Security

Requirements
Must have
• a) Logo
b) Main index page with a new logo and design
c) System (post log in e-wallet) main page showing the last transactions of the client and give client options to transfer funds and make deposits
Nice to have
• sample contact form
sample faq page
terms page design
Should not have
• So much text since it will be aimed at the worldwide market

```html
<!DOCTYPE html>
<html lang="en">
<head>
<meta charset="utf-8">
<title>Pelmora – Online Banking &amp; Money Management</title>
<link rel="stylesheet" href="https://fonts.googleapis.com/css2?family=Roboto:wght@300;400;500;700&family=Montserrat:wght@600;700&display=swap">
<style>
:root{
  --topbar-top:#2a2a2a;
  --topbar-bottom:#050505;
  --field:#4a4a4a;
  --field-border:#5e5e5e;
  --field-text:#e4e4e4;
  --gold-light:#f7d96a;
  --gold:#e9b93a;
  --gold-dark:#b98418;
  --gold-text:#6b4a0c;
  --brand-gold:#b87a1e;
  --ink:#1b1b1b;
  --ink-soft:#555;
  --hero-bg:#e8e8e8;
  --panel:#ffffff;
  --band:#f1f1f1;
  --divider:#e0e0e0;
  --dark-top:#2d2d2d;
  --dark-bottom:#454545;
  --footer-text:#f2f2f2;
}
*{box-sizing:border-box;margin:0;padding:0}
html,body{width:1200px;height:1128px;overflow:hidden}
body{font-family:"Roboto",Arial,sans-serif;background:var(--dark-top);color:var(--ink);position:relative}

.topbar{position:absolute;left:0;top:0;width:1200px;height:62px;background:linear-gradient(90deg,var(--topbar-bottom),var(--topbar-top) 60%,#3a3a3a)}
.field{position:absolute;top:15px;height:32px;width:151px;background:var(--field);border:1px solid var(--field-border);border-radius:3px;color:var(--field-text);font-size:14px;line-height:30px;padding-left:10px}
.field--account{left:559px}
.field--password{left:722px}
.forgot{position:absolute;left:888px;top:15px;line-height:32px;font-size:14px;font-weight:500;color:#eee}
.btn-login{position:absolute;left:1012px;top:15px;width:79px;height:32px;border-radius:3px;background:linear-gradient(#f4f4f4,#c9c9c9);border:1px solid #888;font-size:12px;font-weight:700;color:#333;display:flex;align-items:center;justify-content:center;gap:6px}
.btn-signup{position:absolute;left:1112px;top:15px;width:70px;height:32px;border-radius:3px;background:linear-gradient(var(--gold-light),var(--gold));border:1px solid var(--gold-dark);font-size:12px;font-weight:700;color:#3a2a05;display:flex;align-items:center;justify-content:center}

.header{position:absolute;left:0;top:62px;width:1200px;height:112px;background:linear-gradient(#ffffff,#f0f0f0);box-shadow:0 2px 4px rgba(0,0,0,.18);z-index:2}
.brand{position:absolute;left:50px;top:26px;font-family:"Montserrat",Arial,sans-serif;font-weight:700;font-size:36px;letter-spacing:1px;color:var(--brand-gold);line-height:1}
.tagline{position:absolute;left:49px;top:69px;font-size:11px;letter-spacing:2.6px;color:#666}

.hero{position:absolute;left:0;top:174px;width:1200px;height:646px;background:var(--hero-bg)}
.hero-photo{position:absolute;left:380px;top:0;width:820px;height:442px;background:radial-gradient(ellipse at 45% 55%,#3c3c40 0,#2e3540 35%,rgba(70,80,95,.6) 60%,rgba(232,232,232,0) 80%),linear-gradient(90deg,rgba(232,232,232,0),#4a5260 40%,#3b2a2a 85%,#2f3238)}
.hero-title{position:absolute;left:52px;top:50px;font-weight:300;font-size:56px;line-height:60px;color:#111;letter-spacing:-.5px}
.hero-text{position:absolute;left:55px;top:184px;width:420px;font-size:18px;line-height:25px;color:var(--ink-soft)}
.btn-start{position:absolute;left:55px;top:260px;width:193px;height:56px;border-radius:3px;background:linear-gradient(#5a5d61,#2d2f32);color:#fff;font-size:20px;font-weight:500;display:flex;align-items:center;justify-content:center}

.darkband{position:absolute;left:0;top:820px;width:1200px;height:308px;background:linear-gradient(var(--dark-top),var(--dark-bottom) 50%,#2f2f2f)}

.features{position:absolute;left:48px;top:616px;width:1106px;height:344px;background:var(--panel);border:1px solid #ccc;display:flex;z-index:3}
.feature{flex:1;position:relative;border-left:1px solid var(--divider)}
.feature:first-child{border-left:none}
.feature-art{position:absolute;left:50%;top:28px;transform:translateX(-50%);width:120px;height:112px;border-radius:10px}
.art-gold{background:radial-gradient(circle at 40% 35%,#f6d56a,#c8901e 70%,#8a5a10)}
.art-arrows{background:radial-gradient(circle at 50% 45%,#f3c85a,#c2811c 70%,#7a4a12)}
.art-shield{background:radial-gradient(circle at 40% 40%,#e9b94a,#7a4210 70%,#3b1c08)}
.feature-title{position:absolute;left:0;right:0;top:160px;height:46px;background:var(--band);text-align:center;line-height:46px;font-size:24px;font-weight:400;letter-spacing:.3px;color:#111}
.feature-text{position:absolute;left:40px;right:40px;top:218px;text-align:center;font-size:14.5px;line-height:21px;color:#111}
.btn-more{position:absolute;left:50%;top:282px;transform:translateX(-50%);width:128px;height:33px;border-radius:2px;background:linear-gradient(var(--gold-light),var(--gold));border:1px solid var(--gold-dark);color:var(--gold-text);font-size:12px;font-weight:700;display:flex;align-items:center;justify-content:center}

.footer{position:absolute;left:0;top:990px;width:1200px;text-align:center;color:var(--footer-text)}
.footer-brand{font-family:"Montserrat",Arial,sans-serif;font-weight:700;font-size:22px;letter-spacing:1px;color:var(--gold-light);line-height:30px}
.footer-links{margin-top:10px;font-size:13px;display:flex;justify-content:center;gap:12px}
.footer-links .sep{color:#ccc}
.copyright{margin-top:14px;font-size:12.5px}
</style>
</head>
<body>
<div class="topbar">
  <div class="field field--account">Account Number</div>
  <div class="field field--password">Password</div>
  <div class="forgot">Forgot Password?</div>
  <div class="btn-login">
    <svg width="11" height="13" viewBox="0 0 11 13" aria-hidden="true"><path d="M2.5 6V4a3 3 0 0 1 6 0v2" fill="none" stroke="#444" stroke-width="1.6"/><rect x="1" y="6" width="9" height="7" rx="1" fill="#444"/></svg>
    LOG IN
  </div>
  <div class="btn-signup">SIGN UP</div>
</div>

<header class="header">
  <div class="brand">PELMORA</div>
  <div class="tagline">ONLINE BANKING &amp; MONEY MANAGEMENT</div>
</header>

<section class="hero">
  <div class="hero-photo" role="img" aria-label="Photo of a person holding a tablet showing the online account dashboard"></div>
  <h1 class="hero-title">Manage Pelmora Account<br>Seamlessly on the fly</h1>
  <p class="hero-text">Lorem ipsum dolor sit amet, consectetur adipiicing elit, sed do eiusmod tempor incididunt.</p>
  <div class="btn-start">GET STARTED</div>
</section>

<div class="darkband"></div>

<section class="features">
  <div class="feature">
    <div class="feature-art art-gold" role="img" aria-label="Illustration of stacked gold bars"></div>
    <h2 class="feature-title">HOW IT WORKS</h2>
    <p class="feature-text">Lorem ipsum dolor sit amet, consectetur adipisicing elit, sed do eiusmod tempor</p>
    <div class="btn-more">LEARN MORE</div>
  </div>
  <div class="feature">
    <div class="feature-art art-arrows" role="img" aria-label="Illustration of gold exchange arrows"></div>
    <h2 class="feature-title">TRANSFERS &amp; DEPOSITS</h2>
    <p class="feature-text">Lorem ipsum dolor sit amet, consectetur adipisicing elit, sed do eiusmod tempor</p>
    <div class="btn-more">LEARN MORE</div>
  </div>
  <div class="feature">
    <div class="feature-art art-shield" role="img" aria-label="Illustration of a gold security shield"></div>
    <h2 class="feature-title">SECURITY &amp; TRUST</h2>
    <p class="feature-text">Lorem ipsum dolor sit amet, consectetur adipisicing elit, sed do eiusmod tempor</p>
    <div class="btn-more">LEARN MORE</div>
  </div>
</section>

<footer class="footer">
  <div class="footer-brand">PELMORA</div>
  <nav class="footer-links">
    <span>About Us</span><span class="sep">|</span>
    <span>Contact Us</span><span class="sep">|</span>
    <span>Legal Agreements</span><span class="sep">|</span>
    <span>Privacy</span><span class="sep">|</span>
    <span>Fees</span><span class="sep">|</span>
    <span>Site Feedback</span>
  </nav>
  <p class="copyright">Copyright © 1999-2012 Orvanta. All rights reserved.</p>
</footer>
</body>
</html>
```